Website for Dental Office - The Brightcrest Clinic

The brightcrest clinic is a dental office offering cosmetic dentistry, general dentistry, and multi-specialty dental care all under one roof in our state-of-the-art cosmetic dental center. We are particularly striving to provide services that fit the need of the young generation. Thus, we hope to have a modern, professional concise website that represents our spirit.

*Should be able to switch from English to Chinese

6 sections besides homepage:
Home, Meet us, Services,
Patient Info, Cases&Reviews, Blog, Contact

The Services sections should contain multiple subsections such as cleaning and prevention, cosmetic dentistry, implant dentistry, removable dentures, etc...
The Patient Info section is also intended to contain several subsections such as
New Patient offer, accepted Insurance, patient portal, helpful tips, etc...

Target Market(s)

young generation

Coding

Number of Pages Required

5+ page

Font styles to use
Sans Serif

Colors
0592cd
33a6d7
85cae6
00a990
33b8a4
86cfc6
cee9f5
cfeae6
3277b5

Requirements
Must have
• *Should be able to switch from English to Chinese
Nice to have
• http://www.thebrightcrestclinic-example.com/
• As a reference, the above link is the current website, but we would like to change the appearance and the content (our new logo's picture is attached)

```html
<!DOCTYPE html>
<html lang="en">
<head>
<meta charset="utf-8">
<title>The Brightcrest Clinic – Dental Office</title>
<link href="https://fonts.googleapis.com/css2?family=Open+Sans:wght@400;600;700;800&family=Montserrat:wght@700;800&display=swap" rel="stylesheet">
<style>
:root{
  --blue:#0592cd; --blue-mid:#33a6d7; --blue-light:#85cae6; --blue-pale:#cee9f5;
  --teal:#00a990; --teal-mid:#33b8a4; --teal-light:#86cfc6; --teal-pale:#cfeae6;
  --navy:#3277b5; --mint-bg:#e9f8f7; --aqua-bg:#e3f4f7; --ink:#222; --grey:#777;
  --yellow:#fcdb8a;
}
*{box-sizing:border-box;margin:0;padding:0}
html,body{width:1200px;height:3189px;overflow:hidden}
body{position:relative;font-family:"Open Sans",Arial,sans-serif;color:var(--ink);background:#fff}
.abs{position:absolute}
.stripe{position:absolute;left:0;width:1200px;height:9px;display:flex}
.stripe span{flex:1}
/* header */
.site-header{position:absolute;top:9px;left:0;width:1200px;height:75px;background:#fff;border-bottom:1px solid #e4e4e4}
.brand{position:absolute;left:120px;top:16px;display:flex;align-items:center;gap:12px}
.brand-mark{width:46px;height:44px;background:var(--blue-mid)}
.brand-name{font-weight:700;font-size:22px;line-height:23px;color:var(--blue-mid);text-transform:uppercase}
.main-nav{position:absolute;top:29px;right:114px;display:flex;gap:25px;font-size:16px}
.main-nav a{color:#222;text-decoration:none}
.main-nav a.active{color:var(--teal)}
/* hero */
.hero{position:absolute;top:84px;left:0;width:1200px;height:591px;background:linear-gradient(110deg,#6d94a8 0%,#b9cfd6 30%,#e9f1f3 55%,#dfe6ea 80%,#9fb0b8 100%)}
.hero-dots{position:absolute;top:547px;left:748px;display:flex;gap:10px}
.hero-dots span{width:14px;height:14px;border-radius:50%;background:var(--teal-mid)}
.hero-dots span:first-child{background:var(--teal)}
.lang{position:absolute;top:87px;left:1003px;width:84px;height:72px;background:#fff;text-align:center;border-radius:0 0 3px 3px}
.lang .cur{font-size:18px;margin-top:4px}
.lang .opt{font-size:12px;line-height:21px}
.lang .opt.en{color:var(--teal)}
/* about */
.about{position:absolute;top:675px;left:0;width:1200px;height:900px;background:var(--mint-bg)}
.about-art{position:absolute;left:0;top:216px;width:483px;height:508px;border-radius:40% 40% 20% 20%;background:radial-gradient(ellipse at 55% 45%,#bfe0f7 0%,#dbeefa 40%,#fbe6c9 75%,rgba(233,248,247,0) 100%)}
.eyebrow{font-size:27px;color:var(--teal);font-weight:400}
.h2{font-size:33px;font-weight:600;color:#222}
.lead{font-size:15.5px;line-height:26.5px;color:#777;text-align:justify}
.svc-card{position:absolute;width:277px;height:265px;background:#fff;border:1px solid #bbb;padding:26px 10px 0 10px}
.svc-card h3{font-weight:400;font-size:27px;line-height:31px;color:#222;margin-top:2px}
.svc-card p{font-size:16px;line-height:26.5px;color:#888;margin-top:13px;text-align:justify}
.svc-card .more{display:block;font-weight:700;font-size:15.5px;margin-top:9px;padding-left:4px;color:#222}
.svc-badge{position:absolute;width:94px;height:94px;border-radius:50%;background:var(--teal);right:10px;top:-42px;display:flex;align-items:center;justify-content:center}
/* patient info */
.wave{position:absolute;left:0}
.pi-btn{position:absolute;width:251px;height:93px;display:flex;align-items:center;gap:18px;padding-left:14px;font-family:Montserrat,Arial,sans-serif;font-weight:800;font-size:21px;line-height:29px;color:#fff;letter-spacing:.5px}
.phone-art{position:absolute;left:552px;top:1671px;width:154px;height:384px;border-radius:24px;background:linear-gradient(180deg,#cdeaf8,#8fcdee)}
.visit{position:absolute;left:780px;top:1783px;width:420px;height:272px;background:#fff;box-shadow:0 2px 12px rgba(0,0,0,.18)}
.visit h2{position:absolute;left:43px;top:10px;font-weight:800;font-size:56px;line-height:58px;letter-spacing:1px}
.visit .sub{position:absolute;left:80px;top:140px;font-size:22px;color:#bdbdbd;font-weight:600}
.book{position:absolute;left:57px;top:185px;width:250px;height:59px;background:var(--yellow);color:#fff;font-weight:700;font-size:26px;letter-spacing:1px;display:flex;align-items:center;justify-content:center}
/* discover */
.discover-copy{position:absolute;left:110px;top:2124px;width:400px}
.discover-copy .kicker{font-size:28px;line-height:34px}
.discover-copy h2{font-size:33px;font-weight:700;line-height:38px;margin-top:2px;letter-spacing:.5px}
.discover-copy p{font-size:12.5px;line-height:20.5px;color:#777;margin-top:16px;text-align:justify;width:385px}
.cta{position:absolute;left:111px;top:2371px;width:250px;height:58px;background:var(--teal);color:#fff;font-weight:700;font-size:21px;letter-spacing:.5px;display:flex;align-items:center;justify-content:center}
.icon-panel{position:absolute;left:566px;top:2108px;width:521px;height:321px;background:#fff;box-shadow:0 2px 10px rgba(0,0,0,.12);display:grid;grid-template-columns:repeat(4,1fr);padding:40px 6px 0}
.icon-cell{text-align:center;font-size:13px;letter-spacing:1px;color:#555;height:128px}
.icon-cell svg{display:block;margin:0 auto 8px}
/* video & how */
.media{position:absolute;top:2476px;left:0;width:1200px;height:394px;background:var(--aqua-bg)}
.video{position:absolute;left:113px;top:2579px;width:333px;height:257px;border-radius:10px;background:linear-gradient(135deg,#5aa9d4,#a9d6ec 60%,#6fb3da)}
.acc{position:absolute;left:657px;width:429px;height:46px;border-radius:23px;display:flex;align-items:center;font-family:Montserrat,Arial,sans-serif;font-size:12px;font-weight:700;color:#fff}
.acc .plus{width:36px;height:36px;border-radius:50%;background:#fff;margin:0 24px 0 5px;display:flex;align-items:center;justify-content:center;font-size:20px;font-family:"Open Sans",sans-serif}
.acc-body{position:absolute;left:724px;top:2638px;width:310px;font-size:12.3px;line-height:21px;color:#333;text-align:justify}
/* footer */
.site-footer{position:absolute;top:2880px;left:0;width:1200px;height:309px;background:var(--teal);color:#fff}
.foot-brand{position:absolute;left:113px;top:21px;width:250px;height:64px;background:#fff;display:flex;align-items:center;gap:12px;padding-left:10px}
.foot-brand .brand-mark{width:56px;height:42px;flex:none}
.foot-brand .brand-name{font-size:17px;line-height:20px;white-space:nowrap}
.foot-about{position:absolute;left:113px;top:112px;width:315px;font-size:14px;line-height:26px}
.copy{position:absolute;left:113px;top:281px;font-size:12px}
.foot-h{position:absolute;font-size:26px;font-weight:700}
.quick{position:absolute;left:614px;top:84px;list-style:none;font-size:15.5px;line-height:30px}
.social{position:absolute;top:3113px;width:46px;height:46px;border-radius:50%;border:2px solid #fff}
</style>
</head>
<body>

<div class="stripe" style="top:0">
  <span style="background:var(--teal-light)"></span><span style="background:var(--blue)"></span><span style="background:var(--blue-light)"></span><span style="background:var(--navy)"></span><span style="background:var(--teal)"></span><span style="background:var(--teal-pale)"></span>
</div>

<header class="site-header">
  <div class="brand"><div class="brand-mark"></div><div class="brand-name">The Brightcrest<br>Clinic</div></div>
  <nav class="main-nav">
    <a class="active" href="#">Home</a><a href="#">Meet us</a><a href="#">Services</a><a href="#">Patient Info</a><a href="#">Cases&amp;Reviews</a><a href="#">Blog</a><a href="#">Contact</a>
  </nav>
</header>

<section class="hero" role="img" aria-label="Smiling patient in the dental chair with a dentist at work, shown on a desktop screen"></section>
<div class="hero-dots"><span></span><span></span><span></span></div>
<div class="lang">
  <div class="cur">English ⌄</div>
  <div class="opt en">English</div>
  <div class="opt">Chinese</div>
</div>

<section class="about">
  <div class="about-art" role="img" aria-label="Illustration of a large tooth inspected with a magnifying glass by a dentist and an assistant on a ladder"></div>
</section>
<div class="abs eyebrow" style="left:503px;top:700px">About us</div>
<div class="abs h2" style="left:503px;top:733px">What you should know</div>
<p class="abs lead" style="left:503px;top:792px;width:584px">Lorem Ipsum is simply dummy text of the printing and typesetting industry. Lorem Ipsum has been the industry's standard dummy text ever since the 1500s, when an unknown printer took a galley of type and scrambled it to make a type specimen book. It has survived not only five centuries,</p>

<article class="svc-card" style="left:503px;top:947px">
  <div class="svc-badge"><svg width="50" height="50" viewBox="0 0 50 50" fill="none" stroke="#fff" stroke-width="2.5"><path d="M25 8l8 12H17z"/><path d="M10 38l6-12 8 12z"/><path d="M40 38l-8-12-6 12z"/></svg></div>
  <h3>Cleaning and<br>Prevention</h3>
  <p>Lorem Ipsum is simply dummy text of the printing and typeset-ting industry. Lorem Ipsum has been the industry's</p>
  <span class="more">Read more &gt;</span>
</article>
<article class="svc-card" style="left:810px;top:947px">
  <div class="svc-badge"><svg width="50" height="56" viewBox="0 0 50 56" fill="none" stroke="#fff" stroke-width="2.5"><path d="M10 8c6-5 12 0 15 0s9-5 15 0c6 6 2 16 0 22-2 8-2 22-6 22s-4-14-9-14-5 14-9 14-4-14-6-22c-2-6-6-16 0-22z"/></svg></div>
  <h3>Cosmetic<br>Dentistry</h3>
  <p>Lorem Ipsum is simply dummy text of the printing and typeset-ting industry. Lorem Ipsum has been the industry's</p>
  <span class="more">Read more &gt;</span>
</article>
<article class="svc-card" style="left:503px;top:1270px">
  <div class="svc-badge"><svg width="40" height="60" viewBox="0 0 40 60" fill="none" stroke="#fff" stroke-width="2.5"><path d="M6 6c4-4 8 0 14 0s10-4 14 0c3 4 0 10-2 12H8C6 16 3 10 6 6z"/><path d="M12 24h16M13 31h14M14 38h12M15 45h10M18 52h4"/></svg></div>
  <h3>Implant<br>Dentistry</h3>
  <p>Lorem Ipsum is simply dummy text of the printing and typeset-ting industry. Lorem Ipsum has been the industry's</p>
  <span class="more">Read more &gt;</span>
</article>
<article class="svc-card" style="left:810px;top:1270px">
  <div class="svc-badge"><svg width="64" height="36" viewBox="0 0 64 36" fill="none" stroke="#fff" stroke-width="2.5"><rect x="4" y="8" width="12" height="20" rx="5"/><rect x="18" y="8" width="12" height="20" rx="5"/><rect x="32" y="8" width="12" height="20" rx="5"/><rect x="46" y="8" width="12" height="20" rx="5"/><path d="M2 18h60"/></svg></div>
  <h3>Removable<br>Dentures</h3>
  <p>Lorem Ipsum is simply dummy text of the printing and typeset-ting industry. Lorem Ipsum has been the industry's</p>
  <span class="more">Read more &gt;</span>
</article>

<svg class="wave" style="top:1560px" width="1200" height="80" viewBox="0 0 1200 80"><path d="M0 0H1200V80C1050 30 900 70 720 60 520 50 350 0 170 14 100 20 40 10 0 0Z" fill="var(--mint-bg)"/><path d="M170 14C350 0 520 50 720 60 900 70 1050 30 1200 80 1050 50 900 90 700 72 520 60 330 24 170 14Z" fill="var(--teal-mid)" opacity=".85"/></svg>

<svg class="wave" style="top:2020px" width="1200" height="90" viewBox="0 0 1200 90"><path d="M0 30C200 10 400 60 600 50 800 40 1000 5 1200 40V90H0Z" fill="var(--aqua-bg)"/><path d="M0 22C200 0 420 55 600 40 800 25 1000 0 1200 30V42C1000 8 800 46 600 54 400 62 200 14 0 34Z" fill="var(--teal-light)" opacity=".6"/></svg>

<div class="pi-btn" style="left:106px;top:1648px;background:var(--blue-mid)">
  <svg width="46" height="46" viewBox="0 0 46 46" fill="none" stroke="#fff" stroke-width="2"><circle cx="23" cy="23" r="20" stroke-dasharray="4 3"/><path d="M16 30l14-14"/><circle cx="17" cy="17" r="3"/><circle cx="29" cy="29" r="3"/></svg>
  <span>NEW PATIENT<br>OFFER</span>
</div>
<div class="pi-btn" style="left:836px;top:1648px;background:var(--navy)">
  <svg width="46" height="50" viewBox="0 0 46 50" fill="none" stroke="#fff" stroke-width="2.2"><rect x="3" y="6" width="40" height="41" rx="4"/><path d="M3 14h40M10 2v8M18 2v8M28 2v8M36 2v8"/><path d="M23 20v14M23 39v2"/></svg>
  <span>SPECIAL<br>HELPFUL TIPS</span>
</div>
<div class="pi-btn" style="left:189px;top:1783px;background:var(--teal-pale)">
  <svg width="66" height="66" viewBox="0 0 66 66" fill="none" stroke="#fff" stroke-width="2.2"><path d="M4 30C6 14 20 6 33 6s27 8 29 24c-5-4-10-4-14 0-4-4-10-4-15 0-5-4-11-4-15 0-4-4-9-4-14 0z"/><path d="M33 30v22M22 46l10 12 16-18"/></svg>
  <span>ACCEPTED<br>INSURANCE</span>
</div>
<div class="pi-btn" style="left:110px;top:1916px;background:var(--teal)">
  <svg width="66" height="66" viewBox="0 0 66 66" fill="none" stroke="#fff" stroke-width="2.2"><rect x="8" y="8" width="50" height="50" rx="8"/><rect x="14" y="20" width="38" height="38" rx="4"/><circle cx="33" cy="33" r="6"/><path d="M22 56c0-8 5-12 11-12s11 4 11 12"/></svg>
  <span>PATIENT<br>PORTAL</span>
</div>
<div class="phone-art" role="img" aria-label="Illustration of a smartphone under a cloud showing the clinic app"></div>

<div class="visit">
  <h2>Plan Your<br>Visit Now</h2>
  <div class="sub">Begin the Change</div>
  <div class="book">BOOK NOW</div>
</div>

<div class="discover-copy">
  <div class="kicker">Discover</div>
  <h2>Dental Office - The Brightcrest Clinic</h2>
  <p>Lorem Ipsum is simply dummy text of the printing and typeset-ting industry. Lorem Ipsum has been the industry's standard dummy text ever since the 1500s, when an unknown printer took a galley of type and scrambled it to make a type specimen book.</p>
</div>
<div class="cta">MAKE APPOINMENT</div>

<div class="icon-panel">
  <div class="icon-cell"><svg width="44" height="58" viewBox="0 0 44 58" fill="none" stroke="var(--blue)" stroke-width="2"><path d="M6 6c5-4 10 0 16 0s11-4 16 0c4 4 1 11-1 14H7C5 17 2 10 6 6z"/><path d="M13 26h18M14 33h16M15 40h14M17 47h10"/></svg>IMPLANTS</div>
  <div class="icon-cell"><svg width="60" height="58" viewBox="0 0 60 58" fill="none" stroke="var(--blue)" stroke-width="2"><path d="M16 8c5-4 10 0 14 0s9-4 14 0c5 5 2 14 0 20-2 8-2 24-6 24s-4-14-8-14-4 14-8 14-4-16-6-24c-2-6-5-15 0-20z"/><circle cx="6" cy="38" r="3"/><circle cx="54" cy="38" r="3"/></svg>GUM</div>
  <div class="icon-cell"><svg width="44" height="58" viewBox="0 0 44 58" fill="none" stroke="var(--blue)" stroke-width="2"><path d="M6 8c5-4 10 0 16 0s11-4 16 0c5 5 2 14 0 20-2 8-2 24-6 24s-4-14-10-14-6 14-10 14-4-16-6-24C4 22 1 13 6 8z"/><path d="M16 30l2 16M28 30l-2 16"/></svg>ROOTS</div>
  <div class="icon-cell"><svg width="56" height="58" viewBox="0 0 56 58" fill="none" stroke="var(--blue)" stroke-width="2"><rect x="4" y="12" width="40" height="42"/><path d="M12 22c4-3 8 0 12 0s8-3 12 0c3 4 0 10-1 14-1 6-2 12-4 12s-3-8-7-8-5 8-7 8-3-6-4-12c-1-4-4-10-1-14z"/><circle cx="44" cy="14" r="10"/></svg>X-RAY</div>
  <div class="icon-cell"><svg width="50" height="58" viewBox="0 0 50 58" fill="none" stroke="var(--blue)" stroke-width="2"><path d="M8 10c5-4 10 0 14 0s9-4 14 0c5 5 2 14 0 20-2 8-2 24-6 24s-4-14-8-14-4 14-8 14-4-16-6-24C6 24 3 15 8 10z"/><path d="M40 2v12M34 8h12"/></svg>WHITENING</div>
  <div class="icon-cell"><svg width="58" height="58" viewBox="0 0 58 58" fill="none" stroke="var(--blue)" stroke-width="2"><circle cx="29" cy="29" r="25"/><path d="M18 16c4-3 8 0 11 0s7-3 11 0c4 4 1 10 0 14-1 7-2 16-5 16s-3-10-6-10-3 10-6 10-4-9-5-16c-1-4-4-10 0-14z"/></svg>PREVENTION</div>
  <div class="icon-cell"><svg width="44" height="58" viewBox="0 0 44 58" fill="none" stroke="var(--blue)" stroke-width="2"><path d="M6 8c5-4 10 0 16 0s11-4 16 0c5 5 2 14 0 20-2 8-2 24-6 24s-4-14-10-14-6 14-10 14-4-16-6-24C4 22 1 13 6 8z"/><circle cx="28" cy="16" r="3" fill="var(--blue)"/></svg>CARIES</div>
  <div class="icon-cell"><svg width="46" height="58" viewBox="0 0 46 58" fill="none" stroke="var(--blue)" stroke-width="2"><path d="M4 4h28l10 10v40H4z"/><path d="M32 4v10h10M11 20h22M11 27h22"/><rect x="20" y="34" width="16" height="16"/><path d="M28 37v10M23 42h10"/></svg>IDOCTOR</div>
</div>

<section class="media"></section>
<div class="abs" style="left:118px;top:2510px;font-size:33px;font-weight:700;letter-spacing:.5px">Our Video</div>
<div class="video" role="img" aria-label="Video still of a dentist treating a young patient"></div>
<svg class="abs" style="left:212px;top:2648px" width="116" height="116" viewBox="0 0 116 116"><circle cx="58" cy="58" r="53" fill="none" stroke="#111" stroke-width="9"/><path d="M44 34l40 24-40 24z" fill="#111"/></svg>

<div class="abs" style="left:666px;top:2510px;font-size:33px;font-weight:700;letter-spacing:.5px">How it works</div>
<div class="acc" style="top:2580px;background:var(--teal)"><span class="plus" style="color:var(--teal)">+</span>WHAT METHOD DO YOU USE FOR CLEANING?</div>
<p class="acc-body">Lorem Ipsum is simply dummy text of the printing and typesetting industry. Lorem Ipsum has been the industry's standard dummy text ever since the 1500s,</p>
<div class="acc" style="top:2729px;background:var(--blue-light)"><span class="plus" style="color:var(--blue-light)">+</span>WHAT METHOD DO YOU USE FOR CLEANING?</div>
<div class="acc" style="top:2790px;background:var(--blue-light)"><span class="plus" style="color:var(--blue-light)">+</span>WHAT METHOD DO YOU USE FOR CLEANING?</div>

<div class="stripe" style="top:2870px;height:10px">
  <span style="background:var(--blue-light)"></span><span style="background:var(--blue)"></span><span style="background:var(--blue-light)"></span><span style="background:var(--navy)"></span><span style="background:var(--teal-mid)"></span><span style="background:#222"></span>
</div>

<footer class="site-footer">
  <div class="foot-brand"><div class="brand-mark"></div><div class="brand-name">The Brightcrest<br>Clinic</div></div>
  <p class="foot-about">Lorem Ipsum is simply dummy text of the print-ing and typesetting industry. Lorem Ipsum has been the industry's standard dummy text ever since the 1500s, when an unknown printer took a galley of type and scrambled it to make a type specimen book.</p>
  <div class="copy"><b>THE BRIGHTCREST CLINIC</b> © 2019. All rights reserved.</div>
  <div class="foot-h" style="left:612px;top:28px">Quick links</div>
  <ul class="quick"><li>Home</li><li>Meet us</li><li>Services</li><li>Patient Info</li><li>Cases &amp; Reviews</li><li>Blog</li><li>Contact</li></ul>
  <div class="foot-h" style="left:868px;top:28px">Contact Us</div>
  <div class="abs" style="left:835px;top:88px;display:flex;align-items:center;gap:8px;font-size:20px">
    <svg width="28" height="28" viewBox="0 0 28 28" fill="none" stroke="#fff" stroke-width="2"><circle cx="14" cy="14" r="12"/><path d="M10 8l3 3-2 2c1 2 2 3 4 4l2-2 3 3-2 2c-4 0-9-5-10-10z"/></svg>0100-5550-1234</div>
  <div class="abs" style="left:836px;top:137px;display:flex;align-items:center;gap:10px;font-size:14.5px">
    <svg width="26" height="18" viewBox="0 0 26 18" fill="none" stroke="#fff" stroke-width="1.6"><rect x="1" y="1" width="24" height="16"/><path d="M1 1l12 10L25 1M1 17l9-8M25 17l-9-8"/></svg>support@thebrightcrestclinic-example.com</div>
  <div class="foot-h" style="left:884px;top:183px">Follow Us</div>
</footer>
<div class="social" style="left:872px"></div>
<div class="social" style="left:927px"></div>
<div class="social" style="left:982px"></div>

</body>
</html>
```